Plumbing Company trying to attract new client base for particular works

In need of something to letterbox drop. There is an opportunity to provide "new sewer drains to the new sewer connections on your street".
There will be discounts for pensioners.
We have reviews from clients that are highly satisfied with our work.
Work booked within 1 months of stamped date on flyer will receive a further 10% off.
All work carried out by licences tradespeople.

LOGO will need to be altered to say "tidewell plumbing" rather than contracting

Target Market(s)

Home owners in regional South Australia - age 30+

Industry/Entity Type

It Company

Requirements
Must have
• contact phone number, email, company name,
Nice to have
• images,

```html
<!DOCTYPE html>
<html lang="en">
<head>
<meta charset="utf-8">
<title>Tidewell Plumbing – Sewer Connections Flyer</title>
<link href="https://fonts.googleapis.com/css2?family=Arvo:wght@400;700&family=Roboto+Condensed:wght@300;400&display=swap" rel="stylesheet">
<style>
  :root {
    --yellow: #efcf3c;
    --black: #0d0d0d;
    --white: #ffffff;
    --ink: #1a1a1a;
    --stage: #1c1c1c;
    --photo-sky: #c9ccc6;
    --photo-ground: #8a7c68;
  }
  * { box-sizing: border-box; margin: 0; padding: 0; }
  html, body { width: 1200px; height: 1000px; overflow: hidden; background: var(--stage); }
  .flyer {
    position: absolute; left: 392px; top: 53px;
    width: 416px; height: 882px; overflow: hidden;
    background: var(--white);
    font-family: "Arvo", serif; color: var(--ink);
  }
  .flyer-shapes { position: absolute; inset: 0; }
  .headline { position: absolute; left: 0; width: 100%; text-align: center; }
  .headline-main { top: 28px; font-size: 27px; font-weight: 700; color: var(--black); letter-spacing: 0.3px; }
  .headline-sub { top: 94px; font-size: 19.5px; font-weight: 700; color: var(--black); }
  .headline-link {
    top: 65px; font-size: 15px; color: var(--white); text-transform: uppercase;
    display: flex; align-items: center; justify-content: center; gap: 6px; padding: 0 38px;
  }
  .headline-link::before, .headline-link::after { content: ""; flex: 1; border-top: 1px dashed var(--white); }
  .headline-street { top: 124px; font-size: 15px; color: var(--white); }

  .offer { position: absolute; left: 0; width: 100%; text-align: center; }
  .offer-lead { top: 487px; font-size: 18px; }
  .offer-group { top: 506px; font-size: 26px; color: var(--yellow); }
  .offer-rule { position: absolute; left: 48px; width: 304px; top: 556px; border-top: 1px dashed #555; }
  .offer-terms { top: 580px; font-size: 16px; line-height: 23.5px; }
  .offer-badge {
    position: absolute; left: 108px; top: 656px; width: 188px; height: 53px;
    background: var(--yellow); border-radius: 3px;
    font-size: 36px; font-weight: 700; color: var(--black);
    display: flex; align-items: center; justify-content: center;
  }

  .brand {
    position: absolute; left: 30px; top: 826px;
    display: flex; align-items: center; gap: 8px;
    font-family: "Roboto Condensed", sans-serif; font-weight: 400;
    font-size: 17px; color: var(--black); text-transform: uppercase; letter-spacing: 0.5px;
  }
  .brand-mark { width: 18px; height: 18px; background: var(--black); }
  .contact-divider { position: absolute; left: 224px; top: 785px; height: 78px; border-left: 1px solid var(--white); }
  .contact {
    position: absolute; left: 241px; top: 780px; width: 160px;
    font-family: "Roboto Condensed", sans-serif; color: var(--black);
  }
  .contact-label { font-size: 15px; font-weight: 300; }
  .contact-phone { font-size: 25px; font-weight: 300; line-height: 28px; padding-bottom: 3px; border-bottom: 1px dashed var(--black); }
  .contact-line { font-size: 11px; font-weight: 400; line-height: 15px; margin-top: 2px; }
  .contact-phone + .contact-line { margin-top: 6px; }
</style>
</head>
<body>
<main class="flyer">
  <svg class="flyer-shapes" width="416" height="882" viewBox="0 0 416 882">
    <defs>
      <linearGradient id="photoTone" x1="0" y1="0" x2="0" y2="1">
        <stop offset="0" stop-color="var(--photo-sky)"/>
        <stop offset="0.55" stop-color="var(--photo-ground)"/>
        <stop offset="1" stop-color="var(--white)"/>
      </linearGradient>
    </defs>
    <rect class="photo" x="0" y="170" width="416" height="330" fill="url(#photoTone)"
          role="img" aria-label="Photo of a plumber operating a red mini excavator beside a brick house"/>
    <path class="top-band-edge" fill="var(--black)" d="M0 0 H416 V340 C385 255 300 158 200 156 C110 154 40 172 0 188 Z"/>
    <path class="top-band" fill="var(--yellow)" d="M0 0 H416 V318 C380 235 300 145 200 143 C110 141 40 158 0 172 Z"/>
    <path class="bottom-band-edge" fill="var(--black)" d="M0 770 C60 800 150 805 230 775 C300 748 370 738 416 748 V882 H0 Z"/>
    <path class="bottom-band" fill="var(--yellow)" d="M0 782 C60 810 150 815 230 787 C300 762 370 752 416 760 V882 H0 Z"/>
  </svg>

  <h1 class="headline headline-main">NEW SEWER DRAINS</h1>
  <p class="headline headline-link">to the</p>
  <h2 class="headline headline-sub">NEW SEWER CONNECTIONS</h2>
  <p class="headline headline-street">ON YOUR STREET</p>

  <p class="offer offer-lead">discounts for</p>
  <p class="offer offer-group">PENSIONERS</p>
  <div class="offer-rule"></div>
  <p class="offer offer-terms">Work booked within<br>1 months of stamped date<br>on flyer will receive a further</p>
  <div class="offer-badge">10% off</div>

  <div class="brand"><span class="brand-mark"></span>Tidewell Plumbing</div>
  <div class="contact-divider"></div>
  <div class="contact">
    <p class="contact-label">Call Us:</p>
    <p class="contact-phone">0400 555 218</p>
    <p class="contact-line">info@tidewellplumbing.com</p>
    <p class="contact-line">www.tidewellplumbing.com</p>
  </div>
</main>
</body>
</html>
```